Kinsmen Crest Beard Oil Label for 1oz dropper bottle

Create a label for a 1oz beard oil dropper bottle. The label is 1.5 inches tall and 2.75 inches wide. Our logo is listed in the brief so please use it but it doesnt have to be that prominent. BEARD OIL is the most important verbiage. We like elements of all the attached images but we want our own look and feel.

Target Market(s)

Men with beards

Requirements
Must have
• Kinsmen Crest Logo, BEARD OIL, Flavor (Tobacco Vanilla)

Ingredients
Fractionated Coconut Oil (MCT)
Golden Jojoba Oil
Hemp Seed Oil
Tea Tree Essential Oil
Orange Bitter Essential Oil
Peppermint Supreme Essential Oil
Tallow Aromas
DYE FREE

Directions:
Directions: apply 3-6 drops into your hand...rub oil into hands and apply directly onto beard. For best results massage into skin under beard area and work oil out towards beard. Discontinue use if skin becomes irritated.

100% MADE IN THE USA (American Flag 1 color)
Veteran Owned Co.
Nice to have
• Labels can change color with each flavor or a ring can change color to show flavor.

```html
<!DOCTYPE html>
<html lang="en">
<head>
<meta charset="utf-8">
<title>Kinsmen Crest Beard Oil Label</title>
<link rel="stylesheet" href="https://fonts.googleapis.com/css2?family=Special+Elite&family=Oranienbaum&family=Dancing+Script:wght@600&family=Oswald:wght@700&display=swap">
<style>
  :root {
    --backdrop: #d3d3d3;
    --paper-light: #e9d6b5;
    --paper-mid: #dcc39d;
    --paper-edge: #c9ab80;
    --panel: #5b4331;
    --panel-dark: #4a3526;
    --panel-text: #ecdcc0;
    --ink: #1b1611;
    --rule: #3b3129;
    --tobacco: #421c22;
    --vanilla: #f2ead2;
    --flag: #8a2f2c;
  }
  * { margin: 0; padding: 0; box-sizing: border-box; }
  html, body {
    width: 1044px;
    height: 1200px;
    overflow: hidden;
    background: var(--backdrop);
  }
  .canvas {
    position: relative;
    width: 1044px;
    height: 1200px;
  }
  .label {
    position: absolute;
    left: 42px;
    top: 338px;
    width: 960px;
    height: 523px;
    background:
      radial-gradient(ellipse at 50% 45%, var(--paper-light) 0%, var(--paper-mid) 60%, var(--paper-edge) 100%);
    color: var(--ink);
    overflow: hidden;
  }
  .frame-lines {
    position: absolute;
    inset: 0;
  }
  .info-panel {
    position: absolute;
    top: 93px;
    width: 207px;
    height: 316px;
    border-radius: 46px;
    background: linear-gradient(180deg, var(--panel) 0%, var(--panel-dark) 100%);
    color: var(--panel-text);
    font-family: "Oranienbaum", serif;
    text-align: center;
    padding: 10px 12px 0;
  }
  .info-panel--ingredients { left: 31px; }
  .info-panel--directions { left: 725px; }
  .info-panel__title {
    font-size: 21px;
    letter-spacing: 0.2px;
    text-decoration: underline;
    text-underline-offset: 3px;
    margin-bottom: 18px;
  }
  .info-panel__body {
    font-size: 19.5px;
    line-height: 24.4px;
    letter-spacing: -0.3px;
  }
  .info-panel__note {
    font-size: 20px;
    margin-top: 24px;
  }
  .brand {
    position: absolute;
    left: 280px;
    top: 84px;
    width: 400px;
    text-align: center;
    font-family: "Oranienbaum", serif;
    font-size: 46px;
    line-height: 50px;
    color: var(--ink);
  }
  .brand-mark {
    display: inline-block;
    width: 14px;
    height: 14px;
    border-radius: 50%;
    background: var(--ink);
    vertical-align: middle;
    margin-right: 10px;
  }
  .veteran {
    position: absolute;
    left: 544px;
    top: 138px;
    font-family: "Oranienbaum", serif;
    font-size: 21px;
    color: var(--ink);
  }
  .product-name {
    position: absolute;
    left: 200px;
    top: 178px;
    width: 560px;
    text-align: center;
    font-family: "Special Elite", monospace;
    font-size: 74px;
    line-height: 90px;
    letter-spacing: 1px;
    color: var(--ink);
  }
  .flavor-name {
    position: absolute;
    left: 230px;
    top: 290px;
    width: 500px;
    text-align: center;
    font-family: "Special Elite", monospace;
    font-size: 39px;
    line-height: 48px;
    font-weight: 700;
    -webkit-text-stroke: 0.8px var(--ink);
  }
  .flavor-dot {
    position: absolute;
    top: 351px;
    width: 54px;
    height: 54px;
    border-radius: 50%;
  }
  .flavor-dot--tobacco { left: 321px; background: var(--tobacco); }
  .flavor-dot--vanilla { left: 588px; background: var(--vanilla); }
  .flavored {
    position: absolute;
    left: 381px;
    top: 350px;
    width: 200px;
    text-align: center;
    font-family: "Dancing Script", cursive;
    font-size: 42px;
    line-height: 52px;
  }
  .size {
    position: absolute;
    left: 60px;
    top: 430px;
    width: 180px;
    text-align: center;
    font-family: "Oswald", sans-serif;
    font-weight: 700;
    font-size: 30px;
    line-height: 40px;
  }
  .origin {
    position: absolute;
    left: 330px;
    top: 434px;
    font-family: "Oranienbaum", serif;
    font-size: 25px;
    line-height: 32px;
    -webkit-text-stroke: 0.5px var(--ink);
  }
  .flag {
    position: absolute;
    left: 595px;
    top: 420px;
    width: 59px;
    height: 58px;
    background: var(--flag);
    border: 1px solid var(--rule);
  }
</style>
</head>
<body>
<main class="canvas">
  <section class="label" aria-label="Kinsmen Crest beard oil label">
    <svg class="frame-lines" width="960" height="523" viewBox="0 0 960 523" aria-hidden="true">
      <g stroke="var(--rule)" stroke-width="2.5" fill="none">
        <!-- corner frames -->
        <path d="M20 28 H222 M20 28 V135"/>
        <path d="M940 28 H738 M940 28 V135"/>
        <path d="M20 495 H222 M20 495 V395"/>
        <path d="M940 495 H738 M940 495 V395"/>
        <!-- dividers -->
        <path d="M348 28 H465 M497 28 H615"/>
        <path d="M348 492 H465 M497 492 H615"/>
      </g>
    </svg>
    <div role="img" aria-label="Star ornament" style="position:absolute;left:467px;top:15px;width:28px;height:28px;border-radius:50%;background:var(--rule);opacity:.8"></div>
    <div role="img" aria-label="Star ornament" style="position:absolute;left:467px;top:478px;width:28px;height:28px;border-radius:50%;background:var(--rule);opacity:.8"></div>

    <div class="info-panel info-panel--ingredients">
      <h2 class="info-panel__title">INGREDIENTS:</h2>
      <p class="info-panel__body">Fractionated Coconut Oil (MCT), Golden Jojoba Oil, Hemp Seed Oil, Tea Tree Essential Oil, Orange Bitter Essential Oil, Pepper&shy;mint Supreme Essential Oil, Tallow Aromas.</p>
      <p class="info-panel__note">DYE FREE</p>
    </div>

    <div class="brand"><span class="brand-mark"></span>Kinsmen Crest</div>
    <div class="veteran">Veteran Owned Co.</div>
    <h1 class="product-name">BEARD OIL</h1>
    <div class="flavor-name">Tobacco Vanilla</div>
    <span class="flavor-dot flavor-dot--tobacco"></span>
    <div class="flavored">flavored</div>
    <span class="flavor-dot flavor-dot--vanilla"></span>

    <div class="info-panel info-panel--directions">
      <h2 class="info-panel__title">DIRECTIONS:</h2>
      <p class="info-panel__body">Apply 3-6 drops into your hand...rub oil into hands and apply directly onto beard. For best results massage into skin under beard area and work oil out towards beard. Discontinue use if skin becomes irritated.</p>
    </div>

    <div class="size">~ 1 OZ ~</div>
    <div class="origin">100% MADE IN THE USA</div>
    <div class="flag" role="img" aria-label="American flag, one colour"></div>
  </section>
</main>
</body>
</html>
```